My name is Tomas Berenji, and I have done business with your company several times. I need a business card to represent my business, I own a company by the name of VELMINO Suntan Lotion & Sunscreen.
My requirements are as follow: My company logo in the brightest gold possible, on a black, grainy (sandy) background, with shading around the each element. With the company name in gold, a stylized coconut trees, and some type of wave graphic in gold. "A product of the USA, Staten Island, NY"
"For comments, suggestion, or ordering please contact us at:
velmino42@brisalto.com"

"VELMINO™ Tanning Lotion & Sunscreen―Crafted with Care"

Velmino Tanning Lotion & Sunscreen is the most extraordinary and innovative sun tanning product to emerge in several generations. The constituents of this product are formidable substances that protect the skin against the aftermath of sun exposure−before you exposed yourself to the sun’s rays. The Aloe Vera in this product, along with other oils and cream, are specifically manufactured to lessen the symptoms of extended exposure to the sun. Velmino is designed to provide a Broad Spectrum Protection (50) that assist in the reduction of (UVA) and (UVB) radiation to create a magnificent sun-absorbing, long-lasting, deep dark bronzing experience.
Thank you,
Tomas Berenji
tomasbberenji@nexipost.com

Target Market(s)

Sunscreen

Industry/Entity Type

Business

Contact Information for Business Card

VELMINO™ Tanning Lotion and Sunscreen
Crafted with Care

Velmino Tanning Lotion is the most extraordinary and innovative sun tanning product to emerge in several generations. The constituents of this product are formidable substances that protect the skin against the aftermath of sun exposure−before you exposed yourself to the sun’s rays. The Aloe Vera, in this product, along with other oils and cream, are specifically manufactured to lessen the symptoms of extended exposure to the sun. Velmino protects your skin from dehydration and treat your skin with the products we apply to ourselves after a sunburn−before the sun tanning process begins. Velmino is designed to provide a Broad Spectrum Protection (50) that assist in the reduction of (UVA) and (UVB) radiation to create a magnificent sun-absorbing, long-lasting, deep dark bronzing experience.

Colors
fece3e
acd136

Requirements
Must have
• Black Card Stock with grainy surface, Gold Logo, stylized Coconut Palm Tree, Company Name, email address, and NYC location.
• Modern Layout with Modern fonts and graphics

```html
<!DOCTYPE html>
<html lang="en">
<head>
<meta charset="utf-8">
<title>VELMINO Business Card</title>
<link href="https://fonts.googleapis.com/css2?family=Open+Sans:wght@400;600;700&display=swap" rel="stylesheet">
<style>
  :root {
    --backdrop: #2b2b2b;
    --card-black: #121212;
    --card-edge: #1c1c1c;
    --gold: #e8a92a;
    --gold-bright: #fece3e;
    --gold-deep: #b9781c;
    --text-light: #e6e6e6;
    --divider: #2a2a2a;
  }
  * { margin: 0; padding: 0; box-sizing: border-box; }
  html, body {
    width: 1200px;
    height: 900px;
    overflow: hidden;
    background: var(--backdrop);
    font-family: "Open Sans", Arial, sans-serif;
  }
  .canvas {
    position: relative;
    width: 1200px;
    height: 900px;
  }
  .card {
    position: absolute;
    top: 305px;
    width: 500px;
    height: 290px;
    border-radius: 22px;
    background: radial-gradient(ellipse at 40% 40%, var(--card-edge), var(--card-black) 75%);
    box-shadow: 0 10px 28px rgba(0,0,0,0.55);
  }
  .card--contact { left: 70px; }
  .card--brand { left: 630px; }

  /* Contact side */
  .contact-logo {
    position: absolute;
    left: 34px;
    top: 72px;
    width: 170px;
    display: flex;
    flex-direction: column;
    align-items: center;
    gap: 10px;
  }
  .brand-dot {
    width: 86px;
    height: 86px;
    border-radius: 50%;
    background: radial-gradient(circle at 40% 35%, var(--gold-bright), var(--gold) 55%, var(--gold-deep));
  }
  .brand-name {
    color: var(--gold);
    font-weight: 700;
    font-size: 26px;
    letter-spacing: 2px;
  }
  .contact-divider {
    position: absolute;
    left: 230px;
    top: 40px;
    width: 1px;
    height: 150px;
    background: var(--divider);
  }
  .contact-details {
    position: absolute;
    left: 252px;
    top: 48px;
  }
  .person-name {
    color: var(--gold);
    font-weight: 600;
    font-size: 17px;
    line-height: 1.2;
  }
  .person-title {
    color: var(--text-light);
    font-size: 12px;
    margin-bottom: 18px;
  }
  .contact-list { list-style: none; }
  .contact-list li {
    display: flex;
    align-items: center;
    gap: 10px;
    color: var(--text-light);
    font-size: 13px;
    line-height: 1.65;
  }
  .contact-list svg { width: 11px; height: 11px; fill: var(--gold); flex: none; }
  .contact-note {
    position: absolute;
    left: 0;
    right: 0;
    bottom: 30px;
    text-align: center;
    color: var(--gold);
    font-weight: 600;
    font-size: 15.5px;
    line-height: 1.35;
  }

  /* Brand side */
  .brand-block {
    position: absolute;
    left: 0;
    right: 0;
    top: 46px;
    display: flex;
    flex-direction: column;
    align-items: center;
    gap: 12px;
  }
  .brand-block .brand-dot { width: 96px; height: 96px; }
  .brand-block .brand-name { font-size: 40px; letter-spacing: 3px; }
  .brand-tagline {
    position: absolute;
    left: 0;
    right: 0;
    top: 218px;
    text-align: center;
    color: var(--gold);
    font-weight: 600;
    font-size: 13px;
    line-height: 1.4;
  }
</style>
</head>
<body>
<main class="canvas">
  <section class="card card--contact">
    <div class="contact-logo">
      <div class="brand-dot"></div>
      <div class="brand-name">VELMINO</div>
    </div>
    <div class="contact-divider"></div>
    <div class="contact-details">
      <p class="person-name">Tomas Berenji</p>
      <p class="person-title">Managing Director</p>
      <ul class="contact-list">
        <li>
          <svg viewBox="0 0 24 24" aria-hidden="true"><path d="M6.6 10.8a15 15 0 0 0 6.6 6.6l2.2-2.2c.3-.3.7-.4 1-.2 1.1.4 2.3.6 3.6.6.6 0 1 .4 1 1V20c0 .6-.4 1-1 1A17 17 0 0 1 3 4c0-.6.4-1 1-1h3.5c.6 0 1 .4 1 1 0 1.3.2 2.5.6 3.6.1.3 0 .7-.2 1z"/></svg>
          (044)-555-0182
        </li>
        <li>
          <svg viewBox="0 0 24 24" aria-hidden="true"><path d="M2 5h20v14H2z M2 5l10 8 10-8" /></svg>
          info@brisalto.com
        </li>
        <li>
          <svg viewBox="0 0 24 24" aria-hidden="true"><circle cx="12" cy="12" r="10"/></svg>
          www.brisalto.com
        </li>
      </ul>
    </div>
    <p class="contact-note">For comments, suggestion, or ordering please<br>contact us at: velmino42@brisalto.com</p>
  </section>

  <section class="card card--brand">
    <div class="brand-block">
      <div class="brand-dot"></div>
      <div class="brand-name">VELMINO</div>
    </div>
    <p class="brand-tagline">VELMINO™ Tanning Lotion &amp; Sunscreen?<br>Crafted with Care</p>
  </section>
</main>
</body>
</html>
```